BrPeople Business Cards for SME Experts

We need a business card for a new company based in Clearwater FL called Brightfold of People. BrP is your access to on-demand subject matter experts. The final design should be very clean communicating innovation and expertise. Our logo design is attached.

The Information Age has affected the workforce in that automation and computerization have resulted in higher productivity coupled with net job loss of many knowledgeable employees. Combined with the creation of the internet and search capabilities, the disintermediation of the value chain of Subject Matter Experts (SME) has happened. We no longer need to work through traditional consulting firms for all consulting needs, instead the direct access to the SME, through a leaner and lower cost model is what the market is demanding.
BrPeople is a new marketplace to buy consulting services. The business model is that all consultants (subject matter experts) can become a consulting resource in the marketplace following our guidelines. The consumer can now easily access consultants that they could not find easily before.
In much the way an Zaxo car can be identified and requested, so can a BrPeople Consultant. Each consultant can be identified by: location, expertise, billing rate, and prior experience rating.
By seamlessly connecting consultants to requesters through a new Brightfold of People marketplace, you now will have an easy to use and quicker turnaround to request and staff your consulting needs. Leveraging the BrP app, you can access the subject matter expert you need for your business requirement.

Target Market(s)

Small and medium sized companies; non-profits

Industry/Entity Type

Business Consultant

Contact Information for Business Card

Name
website
email address
Logo
mailing address (debating if I really need...)
twitter
LinkedIn

Requirements
Must have
• the logo I have included in the design; want the colors to be consistent with the logo design

```html
<!DOCTYPE html>
<html lang="en">
<head>
<meta charset="utf-8">
<title>Brightfold of People – Business Card</title>
<link href="https://fonts.googleapis.com/css2?family=Open+Sans:wght@400;600;700&display=swap" rel="stylesheet">
<style>
  :root {
    --navy: #2e3784;
    --teal: #1ea4c6;
    --pale-teal: #d3eaf0;
    --pale-lilac: #d9dbe8;
    --rule: #7d82b0;
    --card: #fbfbfc;
    --backdrop: #ececec;
  }
  html, body {
    margin: 0;
    width: 1200px;
    height: 1022px;
    overflow: hidden;
    background: var(--backdrop);
    font-family: "Open Sans", Arial, sans-serif;
  }
  .card {
    position: absolute;
    left: 100px;
    top: 225px;
    width: 1000px;
    height: 572px;
    background: var(--card);
    border-radius: 22px;
    overflow: hidden;
    box-shadow: 0 2px 10px rgba(0,0,0,0.12);
  }
  .card__decor {
    position: absolute;
    left: 470px;
    top: -60px;
  }
  .card__tab {
    position: absolute;
    right: 0;
    top: 0;
    width: 92px;
    height: 34px;
    background: var(--teal);
    border-bottom-left-radius: 24px;
  }
  .brand {
    position: absolute;
    left: 70px;
    top: 60px;
  }
  .brand__mark {
    width: 96px;
    height: 96px;
    border-radius: 50%;
    background: var(--teal);
  }
  .brand__name {
    margin-top: 18px;
    font-size: 36px;
    font-weight: 700;
    color: var(--navy);
    letter-spacing: 0.5px;
  }
  .person {
    position: absolute;
    left: 70px;
    top: 262px;
    width: 390px;
  }
  .person__name {
    font-size: 34px;
    font-weight: 600;
    color: var(--navy);
    letter-spacing: 2px;
    padding-bottom: 10px;
  }
  .divider {
    position: absolute;
    left: 70px;
    right: 0;
    top: 322px;
    height: 1px;
    background: var(--rule);
  }
  .contacts {
    position: absolute;
    left: 70px;
    top: 352px;
    margin: 0;
    padding: 0;
    list-style: none;
    font-size: 23px;
    color: var(--navy);
    line-height: 35px;
  }
  .contacts li { display: flex; align-items: center; }
  .contacts svg { width: 20px; height: 20px; margin-right: 12px; flex: none; }
  .address {
    position: absolute;
    right: 70px;
    top: 210px;
    text-align: left;
    font-size: 25px;
    color: var(--navy);
    line-height: 34px;
    letter-spacing: 1px;
  }
</style>
</head>
<body>
  <article class="card">
    <svg class="card__decor" width="560" height="560" viewBox="0 0 560 560" aria-hidden="true">
      <circle cx="280" cy="280" r="250" fill="none" stroke="var(--pale-lilac)" stroke-width="34"/>
    </svg>
    <div class="card__tab"></div>

    <header class="brand">
      <div class="brand__mark"></div>
      <div class="brand__name">Brightfold of People</div>
    </header>

    <div class="person">
      <div class="person__name">DANA REYES</div>
    </div>
    <div class="divider"></div>

    <ul class="contacts">
      <li><svg viewBox="0 0 20 20"><circle cx="10" cy="10" r="7" fill="var(--teal)"/></svg>@dana.reyes</li>
      <li><svg viewBox="0 0 20 20"><circle cx="10" cy="10" r="7" fill="var(--navy)"/></svg>dana/reyes.com</li>
      <li><svg viewBox="0 0 20 20"><rect x="2" y="4" width="16" height="12" fill="none" stroke="var(--teal)" stroke-width="1.6"/><path d="M2 4 L10 11 L18 4" fill="none" stroke="var(--teal)" stroke-width="1.6"/></svg>danareyes@mailbox.com</li>
      <li><svg viewBox="0 0 20 20"><circle cx="10" cy="10" r="8" fill="none" stroke="var(--teal)" stroke-width="1.6"/><ellipse cx="10" cy="10" rx="3.5" ry="8" fill="none" stroke="var(--teal)" stroke-width="1.4"/><line x1="2" y1="10" x2="18" y2="10" stroke="var(--teal)" stroke-width="1.4"/></svg>www.brightfoldofpeople.com</li>
    </ul>

    <address class="address" style="font-style:normal">
      418 W ELM ST<br>
      CLEARWATER FL 33756
    </address>
  </article>
</body>
</html>
```